Consulting company needs Business Cards - rough concept provided

I'm looking for someone to take our business card idea and make is slick and polished - to communicate our high-end, sophisticated, serious consulting business. We have a rough layout we did in-house. We are open to ideas on repo-ing elements, adjusting sizes, typefaces etc... within the general concept we've already come up with. We want it to be super-clean and sophisticated. We want to keep the white backgrounds, and blue brand colors. Our goal is to print with painted blue edges on thick cardstock. Thank you!!

```html
<!DOCTYPE html>
<html lang="en">
<head>
<meta charset="utf-8">
<title>Tarnwick Business Card</title>
<link href="https://fonts.googleapis.com/css2?family=Lato:wght@300;400;700;900&display=swap" rel="stylesheet">
<style>
  :root {
    --page-bg: #f1f1f1;
    --card-bg: #ffffff;
    --brand-blue: #0a96dc;
    --edge-blue: #0a86cc;
    --ink: #111111;
    --muted: #b4b4b4;
  }
  * { margin: 0; padding: 0; box-sizing: border-box; }
  html, body {
    width: 1200px; height: 1000px; overflow: hidden;
    background: var(--page-bg);
    font-family: 'Lato', sans-serif;
  }
  .canvas { position: relative; width: 1200px; height: 1000px; }
  .card {
    position: absolute; left: 250px; width: 702px; height: 402px;
    background: var(--card-bg);
    border-radius: 22px;
    box-shadow: -2px 3px 0 var(--edge-blue);
  }
  .card--front { top: 76px; }
  .card--back { top: 522px; }

  .wordmark {
    position: absolute; left: 0; right: 0; top: 78px;
    text-align: center;
    font-weight: 900; font-size: 78px; line-height: 1;
    letter-spacing: 3px;
    color: var(--brand-blue);
  }
  .identity {
    position: absolute; right: 394px; top: 244px;
    text-align: right;
  }
  .identity__name {
    font-weight: 700; font-size: 26px; color: var(--ink);
    font-variant: small-caps; letter-spacing: 0.5px; line-height: 1;
  }
  .identity__title {
    font-size: 16px; color: var(--ink); margin-top: 8px; line-height: 1;
  }
  .divider {
    position: absolute; left: 344px; top: 215px;
    width: 2px; height: 113px; background: var(--brand-blue);
  }
  .contact {
    position: absolute; left: 376px; top: 212px;
    list-style: none; font-size: 15px; color: var(--ink); line-height: 22px;
  }
  .contact__item { display: flex; align-items: flex-start; }
  .contact__item + .contact__item { margin-top: 1px; }
  .contact__item--address { margin-bottom: 7px; }
  .contact__icon { width: 12px; height: 12px; margin: 5px 11px 0 0; flex: none; fill: var(--ink); }

  .manifesto { position: absolute; inset: 0; }
  .manifesto text { font-family: 'Lato', sans-serif; }
  .m-accent { fill: var(--brand-blue); font-weight: 400; }
  .m-muted { fill: var(--muted); font-weight: 300; }
</style>
</head>
<body>
<div class="canvas">

  <section class="card card--front">
    <div class="wordmark">TARNWICK</div>

    <div class="identity">
      <div class="identity__name">Dana Whitlock</div>
      <div class="identity__title">Brand Consultant</div>
    </div>

    <div class="divider"></div>

    <ul class="contact">
      <li class="contact__item contact__item--address">
        <svg class="contact__icon" viewBox="0 0 12 12"><path d="M6 0a4 4 0 0 0-4 4c0 3 4 8 4 8s4-5 4-8a4 4 0 0 0-4-4zm0 5.6A1.6 1.6 0 1 1 6 2.4a1.6 1.6 0 0 1 0 3.2z"/></svg>
        <span>4820 Harbor Lane, Ste 210<br>Fairmont, CA 94021</span>
      </li>
      <li class="contact__item">
        <svg class="contact__icon" viewBox="0 0 12 12"><path d="M2.4 0.5l2 2.2-1 1.4a7 7 0 0 0 4.5 4.5l1.4-1 2.2 2-1.2 1.9C6 11.4 0.6 6 0.5 1.7z"/></svg>
        <span>(555) 013 4471</span>
      </li>
      <li class="contact__item">
        <svg class="contact__icon" viewBox="0 0 12 12"><path d="M1 2.5h10v7H1z M1 2.5l5 4 5-4" /><path d="M1 2.5h10L6 6.5z" fill="#fff"/></svg>
        <span>dana@tarnwick.com</span>
      </li>
      <li class="contact__item">
        <svg class="contact__icon" viewBox="0 0 12 12"><circle cx="6" cy="6" r="5.5"/><path d="M3.5 3.5c1 .3 1.5 1 1.2 2-.4.8.5 1.5 1 2.3M7.5 1.2c-.3 1 .4 1.6 1.3 1.5.8.6.3 1.7 1.8 2" stroke="#fff" stroke-width="0.9" fill="none"/></svg>
        <span>tarnwick.com</span>
      </li>
    </ul>
  </section>

  <section class="card card--back">
    <svg class="manifesto" width="702" height="402" viewBox="0 0 702 402">
      <text x="46" y="75" font-size="33" textLength="610" lengthAdjust="spacing"><tspan class="m-accent">WE HELP </tspan><tspan class="m-muted">[TARGET DEMOGRAPHIC]</tspan></text>
      <text x="46" y="114" font-size="24" textLength="610" lengthAdjust="spacing"><tspan class="m-accent">ACHIEVE </tspan><tspan class="m-muted">[DESIRED EMOTIONAL OUTCOME] </tspan><tspan class="m-accent">BY</tspan></text>
      <text x="46" y="171" font-size="52" textLength="610" lengthAdjust="spacing" class="m-muted">[OUR UNIQUE APPROACH]</text>
      <text x="42" y="288" font-size="132" textLength="616" lengthAdjust="spacing" class="m-accent" style="font-weight:300">BECAUSE</text>
      <text x="46" y="350" font-size="60" textLength="610" lengthAdjust="spacing" class="m-muted">[OUR BRAND BELIEFS]</text>
    </svg>
  </section>

</div>
</body>
</html>
```